QM Studios needs and Interior Design Business card

I can do anything from Commercial to Residential and Free lance. Beginning to end in design selection process.
Need something to catch the eye of potential customers and vendors. From furniture to Tile and Cabinet selections. I can do it all.

Industry/Entity Type

Design Agency

Contact Information for Business Card

QM Studios- Design Consultanting Residential, Commerical
Maybe a cool detail background. Wall paper print that can have some texture

Font styles to use
Serif

Colors
709dcb
34a6d7
b868aa
e667a6
f59296
85acd3
ffffff
000000
5c5c5c

Requirements
Must have
• Square or Rectangular with Rounded edges
• Name
• Address
• Phone
• Email
Nice to have
• Some colored edges More simples not too busy
• Pattern detail in background.
Should not have
• Not too much color

```html
<!DOCTYPE html>
<html lang="en">
<head>
<meta charset="utf-8">
<title>QM Studios – Business Card</title>
<link rel="stylesheet" href="https://fonts.googleapis.com/css2?family=Source+Sans+3:wght@400;600&family=Didact+Gothic&display=swap">
<style>
  :root {
    --stage: #000000;
    --card: #333438;
    --card-edge: #2e2f33;
    --ink: #f2f2f2;
    --accent: #3fa2d9;
    --divider: #45464b;
  }
  html, body {
    margin: 0;
    width: 1200px;
    height: 900px;
    overflow: hidden;
    background: var(--stage);
  }
  .stage { position: relative; width: 1200px; height: 900px; }
  .card {
    position: absolute;
    top: 271px;
    width: 457px;
    height: 281px;
    border-radius: 14px;
    background: radial-gradient(ellipse at 50% 40%, #37383c 0%, var(--card) 55%, var(--card-edge) 100%);
    overflow: hidden;
    font-family: "Source Sans 3", sans-serif;
    color: var(--ink);
  }
  .card--front { left: 137px; }
  .card--back { left: 626px; }

  .brand-name {
    position: absolute;
    font-family: "Didact Gothic", sans-serif;
    color: var(--ink);
    white-space: nowrap;
  }
  .card--front .brand-name {
    left: 126px; top: 122px;
    transform: translateX(-50%);
    font-size: 24px;
    letter-spacing: 2px;
  }
  .divider {
    position: absolute;
    left: 221px; top: 70px;
    width: 1px; height: 140px;
    background: var(--divider);
  }
  .contact { position: absolute; left: 239px; top: 68px; }
  .contact__name { font-size: 20px; color: var(--accent); line-height: 1.1; margin: 0; font-weight: 400; }
  .contact__title { font-size: 13px; margin: 1px 0 0; }
  .contact__address { font-size: 13px; line-height: 14px; margin: 18px 0 0; }
  .contact__row { display: flex; align-items: center; gap: 8px; font-size: 13px; margin-top: 14px; }
  .contact__row + .contact__row { margin-top: 3px; }
  .contact__row svg { width: 10px; height: 10px; fill: var(--accent); }

  .ring {
    position: absolute;
    left: 179px; top: 70px;
    width: 100px; height: 100px;
  }
  .card--back .brand-name {
    left: 50%; top: 175px;
    transform: translateX(-50%);
    font-size: 32px;
    letter-spacing: 6px;
  }
  .tagline {
    position: absolute;
    left: 0; right: 0; top: 223px;
    display: flex; align-items: center; gap: 8px;
    font-size: 13.5px; font-weight: 600;
    color: var(--accent);
    letter-spacing: 0.4px;
    text-transform: uppercase;
    white-space: nowrap;
  }
  .tagline::before, .tagline::after {
    content: ""; flex: 1; height: 2px; background: var(--accent);
  }
</style>
</head>
<body>
<main class="stage">
  <section class="card card--front">
    <div class="brand-name">QM Studios</div>
    <div class="divider"></div>
    <div class="contact">
      <h1 class="contact__name">Marcus Hale</h1>
      <p class="contact__title">Managing Director</p>
      <p class="contact__address">48 Linden Row, Suite 300<br>Harbor Vale, 204518</p>
      <div class="contact__row">
        <svg viewBox="0 0 10 10" aria-hidden="true"><path d="M2 0.5 L3.6 2.6 L2.8 3.6 Q4 6 6.4 7.2 L7.4 6.4 L9.5 8 L8.4 9.5 Q3.5 9 0.5 1.6 Z"/></svg>
        <span>(055)-318-2064</span>
      </div>
      <div class="contact__row">
        <svg viewBox="0 0 10 10" aria-hidden="true"><path d="M0.5 2 H9.5 V8.5 H0.5 Z" /><path d="M0.5 2 L5 5.6 L9.5 2" stroke="#333438" stroke-width="0.9" fill="none"/></svg>
        <span>hello@qmstudios.co</span>
      </div>
    </div>
  </section>

  <section class="card card--back">
    <svg class="ring" viewBox="0 0 100 100" aria-hidden="true">
      <circle cx="50" cy="50" r="48" fill="none" stroke="#f2f2f2" stroke-width="3"/>
    </svg>
    <div class="brand-name">QM Studios</div>
    <div class="tagline">Design Consultanting Residential, Commerical</div>
  </section>
</main>
</body>
</html>
```